Safety Training company business card design

We are after a high quality, professional business card. We are open to a single or double sided card.

The winning designer must provide the card in a format where we can easily change the name and details of the different people in our organization.

Harbor Guard's company colour is lime green.

We provide all aspects of safety advisory and training for the Building, Civil Construction, Mining, Oil and Gas, Manufacturing, Rail, Rural and Retail sectors.

Visit our website www.harborguard.com.au for training competencies we offer along with our other services including RPL's, safety audits, professional development and client support.

Target Market(s)

Those in the Building, Civil Construction, Mining, Oil and Gas, Manufacturing, Rail, Rural and Retail industries.

Industry/Entity Type

Training

Contact Information for Business Card

Harbor Guard
Safety and Training
Dennis Palworth
Director
M 0427 518 266
dennis@harborguard.com.au
www.harborguard.com.au
(2 business addresses:)
Corvin High Risk Training Centre
17 Tandem Parade, Corvin Q 4211 P 3912 5486 F 3912 5174
Brenlow Training Centre
86 Fenwick Street, Brenlow Q 4752 P 4873 2615 F 4873 2249

Colors
9bcb3c

Requirements
Must have
• Lime green must be the main colour. must include HG logo attached, and state Harbor Guard (Safety and Training in smaller/different font).

State something along the lines of:

Nice to have
• We offer remote training and we can come to you.

```html
<!DOCTYPE html>
<html lang="en">
<head>
<meta charset="utf-8">
<title>Harbor Guard – Business Card</title>
<link href="https://fonts.googleapis.com/css2?family=Oswald:wght@600&family=Lato:wght@300;400;700&display=swap" rel="stylesheet">
<style>
  :root {
    --stage: #1f1f1f;
    --lime: #7dc83a;
    --lime-deep: #5fa52b;
    --forest: #0f6a2f;
    --paper: #ffffff;
    --paper-shade: #eeeeee;
    --ink: #3b3b3b;
    --ink-soft: #6a6a6a;
    --accent: #7dc83a;
  }
  * { box-sizing: border-box; margin: 0; padding: 0; }
  html, body { width: 1200px; height: 900px; overflow: hidden; }
  body {
    background: var(--stage);
    font-family: "Lato", Arial, sans-serif;
    position: relative;
  }
  .card {
    position: absolute;
    top: 175px;
    width: 330px;
    height: 550px;
    border-top: 14px solid var(--forest);
    border-bottom: 14px solid var(--forest);
  }
  /* ---------- contact side ---------- */
  .card--contact {
    left: 205px;
    background: linear-gradient(160deg, var(--paper) 40%, var(--paper-shade));
    padding: 44px 30px 0 30px;
    color: var(--ink);
  }
  .brand { text-align: right; }
  .brand__name {
    font-family: "Oswald", "Arial Narrow", sans-serif;
    font-weight: 600;
    font-size: 40px;
    line-height: 1;
    letter-spacing: 0.5px;
    text-transform: uppercase;
    color: var(--ink);
  }
  .brand__rule {
    height: 1px;
    background: var(--ink-soft);
    margin: 8px 0 7px 20px;
  }
  .brand__tagline {
    font-size: 11px;
    font-weight: 400;
    letter-spacing: 5px;
    text-transform: uppercase;
    color: var(--ink-soft);
  }
  .person { margin-top: 44px; }
  .person__name {
    font-weight: 700;
    font-size: 14px;
    letter-spacing: 0.5px;
    text-transform: uppercase;
    color: var(--accent);
  }
  .person__role {
    font-weight: 700;
    font-size: 10px;
    text-transform: uppercase;
    color: var(--ink);
    margin-top: 2px;
  }
  .contacts { list-style: none; margin-top: 22px; }
  .contacts__item {
    display: flex;
    align-items: flex-start;
    gap: 10px;
    font-size: 11.5px;
    font-weight: 300;
    line-height: 1.55;
    color: var(--ink-soft);
    margin-bottom: 10px;
  }
  .contacts__icon { flex: none; width: 16px; height: 16px; margin-top: 1px; }
  /* ---------- brand side ---------- */
  .card--brand {
    left: 665px;
    background: linear-gradient(170deg, var(--lime) 30%, var(--lime-deep));
    color: var(--paper);
  }
  .offer {
    position: absolute;
    top: 34px;
    left: 0;
    right: 0;
    text-align: center;
    font-weight: 700;
    font-size: 11.5px;
    line-height: 1.45;
    letter-spacing: 1px;
    text-transform: uppercase;
    color: #e8f5da;
  }
  .monogram {
    position: absolute;
    top: 50%;
    left: 0;
    right: 0;
    transform: translateY(-55%);
    text-align: center;
    font-family: "Lato", Arial, sans-serif;
    font-weight: 300;
    font-size: 110px;
    letter-spacing: 4px;
    color: #f2f2f2;
  }
  .website {
    position: absolute;
    bottom: 28px;
    left: 0;
    right: 0;
    text-align: center;
    font-weight: 700;
    font-size: 15px;
    letter-spacing: 0.5px;
    color: var(--paper);
  }
</style>
</head>
<body>

  <section class="card card--contact" aria-label="Contact side">
    <header class="brand">
      <div class="brand__name">Harbor Guard</div>
      <div class="brand__rule"></div>
      <div class="brand__tagline">Safety and Training</div>
    </header>

    <div class="person">
      <div class="person__name">Dennis Palworth</div>
      <div class="person__role">Director</div>
    </div>

    <ul class="contacts">
      <li class="contacts__item">
        <svg class="contacts__icon" viewBox="0 0 16 16" aria-hidden="true">
          <circle cx="8" cy="8" r="8" fill="var(--accent)"/>
          <path d="M5.6 4.2l1.3 1.6-.7 1c.5 1 1.2 1.7 2.1 2.2l1-.7 1.6 1.3-.8 1.2c-2.6-.4-4.6-2.4-5-5z" fill="#fff"/>
        </svg>
        <span>0427 518 266</span>
      </li>
      <li class="contacts__item">
        <svg class="contacts__icon" viewBox="0 0 16 16" aria-hidden="true">
          <circle cx="8" cy="8" r="8" fill="var(--accent)"/>
          <rect x="4.2" y="5.3" width="7.6" height="5.4" fill="none" stroke="#fff" stroke-width="1"/>
          <path d="M4.2 5.4L8 8.3l3.8-2.9" fill="none" stroke="#fff" stroke-width="1"/>
        </svg>
        <span>dennis@harborguard.com.au</span>
      </li>
      <li class="contacts__item">
        <svg class="contacts__icon" viewBox="0 0 16 16" aria-hidden="true">
          <circle cx="8" cy="8" r="8" fill="var(--accent)"/>
          <path d="M8 3.6a2.7 2.7 0 0 0-2.7 2.7C5.3 8.4 8 12 8 12s2.7-3.6 2.7-5.7A2.7 2.7 0 0 0 8 3.6z" fill="#fff"/>
          <circle cx="8" cy="6.3" r="1" fill="var(--accent)"/>
        </svg>
        <span>
          Corvin High Risk Training Centre<br>
          17 Tandem Parade, Corvin Q 4211<br>
          P 3912 5486 F 3912 5174<br>
          Brenlow Training Centre<br>
          86 Fenwick Street, Brenlow Q 4752<br>
          P 4873 2615 F 4873 2249
        </span>
      </li>
    </ul>
  </section>

  <section class="card card--brand" aria-label="Brand side">
    <p class="offer">We offer remote training<br>and we can come to you</p>
    <div class="monogram">HG</div>
    <p class="website">www.harborguard.com.au</p>
  </section>

</body>
</html>
```